Quiet Harbor
How Opening the Palate Renews Rest, Vigor, and Poise Without an Operation
Creative Brief
Description: I’m seeking a talented designer to create a professional, simple, and wellness-oriented cover for my upcoming book. The book explores the hidden connection between jaw expansion, airway health, and whole-body wellness. What I’m Looking For: Clean, minimalist style (similar to Tidal by Colin Marsby and The Lumen Method by Gregory Tallisant). A design that communicates both trustworthiness and transformation — this is a serious wellness/health book, not a textbook. Imagery that subtly conveys space, breathing, and expansion (abstract or symbolic — not literal medical images). Professional typography with good spacing and balance. A design that looks credible in both print and digital formats (Amazon, bookstore, audiobook). Deliverables: Front cover design (with title, subtitle, author name). Full jacket design (front, spine, back cover with provided text). Final files in print-ready PDF + high-res PNG/JPEG + source files (AI/PSD/INDD). About the Author: Dr. Darren Okafield, DMD, is a board-certified orthodontist and dentofacial orthopedist recognized internationally for his airway-focused approach. Featured in Plain Ease, Vantage Wellbeing, and BX Magazine, he helps patients achieve healthier smiles and better breathing without unnecessary surgery.
Health
Health minded people. Men and women but maybe lean a little more toward women
Design the front and back cover. Attached is a current design but I want to go with a new title subtitle of: Title: Open Passage Subtitle: The Quiet Link Among Inhaling, Rest, and Total Vitality ... I'm also open to other titles that might convey a similar message. Here is the back of the book description: What if the cause of your fatigue, poor sleep, anxiety, or lack of focus wasn’t in your mind—but in your mouth? Hidden jaw and airway problems affect millions of adults, yet most go undiagnosed. A narrow palate, mouth breathing, or underdeveloped jaws can quietly disrupt your health, appearance, and energy every single day. In this groundbreaking book, Dr. Darren Okafield—board-certified orthodontist, dentofacial orthopedist, airway-focused clinician, and author of The Kolvex Principle—reveals how your smile, facial balance, and airway are deeply connected to whole-body health. Through real patient stories, simple science, and clear explanations of modern treatment approaches, you’ll discover: The hidden epidemic of underdeveloped jaws and how it impacts breathing, sleep, wellness, and facial harmony Why mouth breathing is more than a bad habit—it’s a health disruptor The truth about palate expanders for adults and children (and what’s important to know about them) What to expect on your treatment journey, from first consultation to long-term results How better breathing can transform not only your health—but also your confidence and overall vitality This isn’t just about teeth. It’s about unlocking the power of proper breathing, creating balance in the face, and giving your body the space it needs to thrive. If you’ve ever felt like something was “off” with your health but couldn’t find the root cause, this book offers the missing link—and a guide to lasting transformation. About the Author Dr. Darren Okafield is a board-certified orthodontist and dentofacial orthopedist and founder of TrelbyBraceClinic.example. Recognized internationally for his airway-focused approach, he helps children, teens, and adults achieve healthier smiles and better breathing without unnecessary surgery. Featured in Plain Ease, Vantage Wellbeing, and with an upcoming expert feature in BX Magazine, he is passionate about educating both consumers and professionals on the life-changing connection between orthodontics, facial development, and whole-body health.

```html
<!DOCTYPE html>
<html lang="en">
<head>
<meta charset="utf-8">
<title>Open Passage — Book Jacket</title>
<link href="https://fonts.googleapis.com/css2?family=Bodoni+Moda:wght@500;600&family=Libre+Baskerville:wght@400;700&display=swap" rel="stylesheet">
<style>
  :root {
    --backdrop: #e9e9e9;
    --cover-light: #8fcde3;
    --cover-mid: #72bcd8;
    --cover-deep: #5eaccc;
    --ink: #1c2b47;
    --ink-soft: #22324f;
    --glow-core: #fff6d8;
    --glow-edge: rgba(255, 246, 216, 0);
  }
  * { margin: 0; padding: 0; box-sizing: border-box; }
  html, body {
    width: 1200px; height: 901px; overflow: hidden;
    background: var(--backdrop);
  }
  .jacket { position: relative; width: 1200px; height: 901px; }
  .cover {
    position: absolute; top: 70px; height: 770px; overflow: hidden;
    background: linear-gradient(160deg, var(--cover-light) 0%, var(--cover-mid) 55%, var(--cover-deep) 100%);
    color: var(--ink);
  }
  .cover--back { left: 70px; width: 510px; }
  .cover--front { left: 612px; width: 520px; }

  .glow {
    position: absolute; border-radius: 50%;
    background: radial-gradient(circle, var(--glow-core) 0%, rgba(255,246,216,.7) 30%, var(--glow-edge) 70%);
  }

  /* Back cover */
  .back-head { position: absolute; top: 92px; left: 0; width: 100%; text-align: center; }
  .back-head .glow { left: 90px; top: 4px; width: 96px; height: 96px; }
  .back-title {
    position: relative; display: inline-block; text-align: left;
    margin-left: 40px;
    font-family: "Bodoni Moda", serif; font-weight: 500;
    font-size: 48px; line-height: 50px; color: var(--ink);
  }
  .back-subtitle {
    position: absolute; top: 228px; left: 60px; width: 390px;
    text-align: center;
    font-family: "Libre Baskerville", serif; font-weight: 700;
    font-size: 12px; line-height: 18px; color: var(--ink);
  }
  .back-copy {
    position: absolute; top: 300px; left: 42px; width: 426px;
    font-family: "Libre Baskerville", serif; font-size: 7.4px; line-height: 11.2px;
    color: var(--ink-soft); text-align: justify;
  }
  .back-copy p { margin-bottom: 8px; }

  /* Front cover */
  .front-head {
    position: absolute; top: 82px; left: 0; width: 100%; text-align: center;
  }
  .front-title {
    display: inline-block; text-align: left;
    font-family: "Bodoni Moda", serif; font-weight: 500;
    font-size: 84px; line-height: 90px; color: var(--ink);
  }
  .cover--front .glow { left: 30px; top: 358px; width: 200px; height: 200px; }
  .front-subtitle {
    position: absolute; top: 392px; left: 230px; width: 250px;
    font-family: "Libre Baskerville", serif; font-weight: 700;
    font-size: 19px; line-height: 29px; color: var(--ink);
  }
  .front-author {
    position: absolute; top: 688px; left: 0; width: 100%; text-align: center;
    font-family: "Libre Baskerville", serif; font-weight: 700;
    font-size: 20px; letter-spacing: 2px; color: var(--ink);
  }
</style>
</head>
<body>
<main class="jacket">

  <section class="cover cover--back" aria-label="Back cover">
    <div class="back-head">
      <div class="glow" role="img" aria-label="Radiant breath emblem"></div>
      <h2 class="back-title">Open<br>Passage</h2>
    </div>
    <p class="back-subtitle">The Quiet Link Among Inhaling, Rest, and Total Vitality</p>
    <div class="back-copy">
      <p>What if the cause of your fatigue, poor sleep, anxiety, or lack of focus wasn’t in your mind—but in your mouth? Hidden jaw and airway problems affect millions of adults, yet most go undiagnosed. A narrow palate, mouth breathing, or underdeveloped jaws can quietly disrupt your health, appearance, and energy every single day.</p>
      <p>In this groundbreaking book, Dr. Darren Okafield—board-certified orthodontist, dentofacial orthopedist, airway-focused clinician, and author of The Kolvex Principle—reveals how your smile, facial balance, and airway are deeply connected to whole-body health. Through real patient stories, simple science, and clear explanations of modern treatment approaches, you’ll discover: the hidden epidemic of underdeveloped jaws and how it impacts breathing, sleep, wellness, and facial harmony; why mouth breathing is more than a bad habit—it’s a health disruptor; the truth about palate expanders for adults and children (and what’s important to know about them); what to expect on your treatment journey, from first consultation to long-term results; how better breathing can transform not only your health—but also your confidence and overall vitality.</p>
      <p>This isn’t just about teeth. It’s about unlocking the power of proper breathing, creating balance in the face, and giving your body the space it needs to thrive. If you’ve ever felt like something was “off” with your health but couldn’t find the root cause, this book offers the missing link—and a guide to lasting transformation.</p>
      <p>About the Author: Dr. Darren Okafield is a board-certified orthodontist and dentofacial orthopedist and founder of TrelbyBraceClinic.example. Recognized internationally for his airway-focused approach, he helps children, teens, and adults achieve healthier smiles and better breathing without unnecessary surgery. Featured in Plain Ease, Vantage Wellbeing, and with an upcoming expert feature in BX Magazine, he is passionate about educating both consumers and professionals on the life-changing connection between orthodontics, facial development, and whole-body health.</p>
    </div>
  </section>

  <section class="cover cover--front" aria-label="Front cover">
    <div class="front-head">
      <h1 class="front-title">Open<br>Passage</h1>
    </div>
    <div class="glow" role="img" aria-label="Radiant breath emblem"></div>
    <p class="front-subtitle">The Quiet Link Among Inhaling, Rest, and Total Vitality.</p>
    <p class="front-author">DARREN OKAFIELD, DMD</p>
  </section>

</main>
</body>
</html>
```